Home Page and One Inside Page Needed for Engine Modify Site

Website that sells kits to modify and enhance your car engine performance. I don't like direction / design of current site at http://www.vortalmotorhaus.com.php61-24.sto3-2.pagedraftzone.com/

I want something modern. Something that shows power and performance.

I need home page and one inside page.

Keep blues and blacks and unfortunately that is their logo we have to work with. But this site needs WOW factor.

YOU DO NOT HAVE PERMISSION TO WORK OR SPEAK TO CLIENT DIRECTLY AND MUST WORK THROUGH ME.

```html
<!DOCTYPE html>
<html lang="en">
<head>
<meta charset="utf-8">
<title>vortalmotorhaus — precision exhaust header modeling system</title>
<link href="https://fonts.googleapis.com/css2?family=Arimo:wght@400;700&display=swap" rel="stylesheet">
<style>
  :root {
    --brand-blue: #0b0be6;
    --nav-blue: #0a0af5;
    --ink: #111111;
    --white: #ffffff;
    --header-bg: #ececec;
    --topbar: #2a2a2a;
    --hero-dark: #030303;
    --band-dark: #3e3e3e;
    --band-mid: #8e8e8e;
    --footer-bg: #2b2b2b;
    --nav-active: #1a1a3a;
    --glow-blue: #1d4fd8;
    --glow-red: #e01818;
    --chrome: #d6d6d6;
  }
  * { box-sizing: border-box; margin: 0; padding: 0; }
  html, body { width: 945px; height: 1200px; overflow: hidden; }
  body { font-family: "Arimo", Arial, sans-serif; background: var(--white); position: relative; }

  .top-strip { position: absolute; left: 0; top: 0; width: 945px; height: 9px; background: var(--topbar); }

  .site-header { position: absolute; left: 0; top: 9px; width: 945px; height: 75px; background: var(--header-bg); border-bottom: 1px solid #cfcfcf; }
  .brand { position: absolute; left: 48px; top: 11px; }
  .brand-name { font-size: 30px; font-weight: 700; color: var(--brand-blue); line-height: 34px; }
  .brand-tag { font-size: 11px; color: var(--ink); margin-top: -2px; }

  .social { position: absolute; display: flex; gap: 10px; align-items: center; }
  .header-social { right: 47px; top: 11px; }
  .dot-icon { width: 14px; height: 14px; border-radius: 50%; background: var(--brand-blue); }
  .mail-icon { width: 16px; height: 11px; }

  .search { position: absolute; left: 738px; top: 34px; width: 162px; height: 25px; border: 1px solid #c5c5c5; border-radius: 12px; background: #f7f7f7; display: flex; align-items: center; padding: 0 6px; gap: 6px; }
  .search-field { font-size: 11px; color: #2222aa; flex: 1; border-left: 1px solid #d0d0d0; padding-left: 5px; }
  .search-btn { width: 22px; height: 12px; border-radius: 6px; background: #4a4af0; }

  .main-nav { position: absolute; left: 0; top: 90px; width: 945px; height: 37px; background: var(--nav-blue); }
  .main-nav a { position: absolute; top: 10px; font-size: 13px; font-weight: 700; color: var(--white); text-decoration: none; }
  .main-nav a.active { color: var(--nav-active); }

  .hero { position: absolute; left: 0; top: 127px; width: 945px; height: 612px; background: var(--hero-dark); overflow: hidden; }
  .hero-art { position: absolute; inset: 0;
    background:
      linear-gradient(172deg, transparent 0%, transparent 6%, rgba(29,79,216,0.85) 12%, rgba(14,40,130,0.55) 20%, transparent 27%),
      radial-gradient(ellipse 9% 7% at 74% 47%, rgba(255,40,40,0.95) 0%, rgba(224,24,24,0.5) 45%, transparent 100%),
      radial-gradient(ellipse 22% 10% at 62% 50%, rgba(180,10,10,0.55) 0%, transparent 100%),
      radial-gradient(ellipse 10% 9% at 57% 64%, rgba(70,110,255,0.9) 0%, rgba(40,70,220,0.4) 50%, transparent 100%),
      radial-gradient(ellipse 12% 8% at 60% 86%, rgba(90,110,255,0.55) 0%, transparent 100%),
      radial-gradient(ellipse 26% 26% at 55% 60%, #bdbdc2 0%, #6c6c72 35%, #26262a 70%, transparent 100%),
      radial-gradient(ellipse 62% 20% at 60% 92%, #7a7a7a 0%, #303030 50%, transparent 100%),
      linear-gradient(90deg, #3a3a3a 0%, #121212 18%, #040404 45%, #060606 85%, #1c1c1c 100%); }
  .hero-title { position: absolute; left: 67px; top: 154px; font-size: 27px; font-weight: 400; color: var(--white); }
  .hero-arrow { position: absolute; top: 270px; width: 20px; height: 32px; }
  .hero-arrow.prev { left: 46px; }
  .hero-arrow.next { left: 878px; }
  .hero-dots { position: absolute; left: 766px; top: 588px; display: flex; gap: 7px; }
  .hero-dots span { width: 13px; height: 13px; border-radius: 50%; background: #3a3a3a; border: 2px solid #555; }
  .hero-dots span.current { background: var(--white); border-color: #777; }

  .features { position: absolute; left: 0; top: 739px; width: 945px; height: 226px; background: linear-gradient(180deg, #4a4a4a, var(--band-dark)); }
  .feature-card { position: absolute; top: 11px; width: 273px; height: 203px; overflow: hidden; }
  .feature-art { position: absolute; inset: 0; }
  .feature-art.alternator { background:
      radial-gradient(ellipse 40% 45% at 55% 62%, #a8a49a 0%, #6e6a62 45%, transparent 80%),
      radial-gradient(ellipse 30% 50% at 8% 60%, #1e1e1e 0%, transparent 100%),
      linear-gradient(180deg, #cfcfcf 0%, #8c8c8c 50%, #4a4a4a 80%, #c8ccd4 100%); }
  .feature-art.airflow { background:
      radial-gradient(ellipse 50% 30% at 45% 60%, #f2f2f2 0%, #bcbcbc 50%, transparent 100%),
      linear-gradient(180deg, #e4e4e4 0%, #b0b0b0 45%, #7a7a7a 70%, #d4d4d4 100%); }
  .feature-art.bay { background:
      radial-gradient(ellipse 60% 30% at 50% 48%, #2a2a2a 0%, #555 60%, transparent 100%),
      linear-gradient(180deg, #c0c0c0 0%, #606060 35%, #3a3a3a 60%, #f0f0f0 85%, #a8a8a8 100%); }
  .feature-label { position: absolute; left: 0; top: 0; width: 100%; height: 50px; background: rgba(235,235,235,0.82); font-size: 16px; color: var(--ink); padding: 19px 0 0 14px; text-transform: uppercase; }

  .thumbs { position: absolute; left: 0; top: 965px; width: 945px; height: 170px; background: var(--band-mid); }
  .thumb { position: absolute; top: 35px; width: 158px; height: 107px; }
  .thumb.glow { background: radial-gradient(ellipse 45% 40% at 45% 50%, #5ff4ff 0%, #13c6d4 45%, #0a3a40 80%), #061a1c; }
  .thumb.bay { background: linear-gradient(180deg, #3a3a3a 0%, #1c1c1c 40%, #8a8a8a 75%, #f2f2f2 100%); }
  .thumb.pipes { background: linear-gradient(90deg, #4a443c 0%, #c4b6a2 22%, #6a6258 40%, #d2c4b0 60%, #5a5248 80%, #b0a290 100%); }
  .thumb.engine { background: radial-gradient(ellipse 38% 40% at 50% 50%, #3a3a3a 0%, #8a8a8a 55%, #ffffff 100%); }
  .thumb.engine-red { background: radial-gradient(ellipse 10% 10% at 38% 40%, #c02020 0%, transparent 100%), radial-gradient(ellipse 40% 42% at 50% 50%, #2a2a2a 0%, #7a7a7a 55%, #ffffff 100%); }
  .thumb-arrow { position: absolute; top: 83px; width: 0; height: 0; border-top: 7px solid transparent; border-bottom: 7px solid transparent; }
  .thumb-arrow.prev { left: 28px; border-right: 10px solid #5a5a5a; }
  .thumb-arrow.next { left: 906px; border-left: 10px solid #5a5a5a; }

  .site-footer { position: absolute; left: 0; top: 1135px; width: 945px; height: 65px; background: var(--footer-bg); }
  .footer-brand { position: absolute; left: 46px; top: 14px; color: var(--white); }
  .footer-brand .brand-name { font-size: 22px; color: var(--white); line-height: 24px; font-weight: 700; }
  .footer-brand .brand-tag { font-size: 8px; color: var(--white); margin-top: 0; }
  .footer-nav a { position: absolute; top: 25px; font-size: 13px; font-weight: 700; color: var(--white); text-decoration: none; }
  .footer-social { left: 832px; top: 25px; }
  .footer-social .dot-icon { background: var(--white); }
</style>
</head>
<body>
  <div class="top-strip"></div>

  <header class="site-header">
    <div class="brand">
      <div class="brand-name">vortalmotorhaus</div>
      <div class="brand-tag">precision exhaust&nbsp; header modeling system</div>
    </div>
    <div class="social header-social">
      <span class="dot-icon"></span>
      <span class="dot-icon"></span>
      <svg class="mail-icon" viewBox="0 0 16 11"><rect x="0.5" y="0.5" width="15" height="10" fill="none" stroke="#0b0be6"/><path d="M0.5 0.5 L8 6.5 L15.5 0.5" fill="none" stroke="#0b0be6"/></svg>
    </div>
    <div class="search">
      <svg width="12" height="12" viewBox="0 0 12 12"><circle cx="5" cy="5" r="3.8" fill="none" stroke="#555" stroke-width="1.5"/><path d="M7.8 7.8 L11 11" stroke="#555" stroke-width="1.5"/></svg>
      <span class="search-field">search</span>
      <span class="search-btn"></span>
    </div>
  </header>

  <nav class="main-nav">
    <a class="active" style="left:49px">Home</a>
    <a style="left:127px">About</a>
    <a style="left:210px">How It Works</a>
    <a style="left:336px">Product</a>
    <a style="left:424px">Resources</a>
    <a style="left:532px">Gallery</a>
    <a style="left:772px">Contact Us</a>
    <a style="left:854px">Sign up</a>
  </nav>

  <section class="hero">
    <div class="hero-art" role="img" aria-label="Concept sports car on a lit glass floor with blue and red exhaust glow, blue car silhouette above"></div>
    <h1 class="hero-title">Precision Exhaust&nbsp; Header Modeling System</h1>
    <svg class="hero-arrow prev" viewBox="0 0 20 32"><path d="M17 2 L3 16 L17 30" fill="none" stroke="#fff" stroke-width="3.5"/></svg>
    <svg class="hero-arrow next" viewBox="0 0 20 32"><path d="M3 2 L17 16 L3 30" fill="none" stroke="#fff" stroke-width="3.5"/></svg>
    <div class="hero-dots"><span class="current"></span><span></span><span></span><span></span><span></span></div>
  </section>

  <section class="features">
    <article class="feature-card" style="left:42px">
      <div class="feature-art alternator" role="img" aria-label="Close-up of an alternator and engine component"></div>
      <div class="feature-label">System Features</div>
    </article>
    <article class="feature-card" style="left:338px">
      <div class="feature-art airflow" role="img" aria-label="Front of a silver car with exhaust airflow lines"></div>
      <div class="feature-label">Who Is Using It?</div>
    </article>
    <article class="feature-card" style="left:633px">
      <div class="feature-art bay" role="img" aria-label="Engine bay of a modern car seen from the front"></div>
      <div class="feature-label">Categories</div>
    </article>
  </section>

  <section class="thumbs">
    <span class="thumb-arrow prev"></span>
    <div class="thumb glow" style="left:56px" role="img" aria-label="Glowing cyan turbine concept"></div>
    <div class="thumb bay" style="left:226px" role="img" aria-label="Engine bay under the hood"></div>
    <div class="thumb pipes" style="left:395px" role="img" aria-label="Polished exhaust header pipes"></div>
    <div class="thumb engine-red" style="left:563px" role="img" aria-label="Turbocharged engine block on white"></div>
    <div class="thumb engine" style="left:731px" role="img" aria-label="Racing engine assembly on white"></div>
    <span class="thumb-arrow next"></span>
  </section>

  <footer class="site-footer">
    <div class="footer-brand">
      <div class="brand-name">vortalmotorhaus</div>
      <div class="brand-tag">precision exhaust&nbsp; header modeling system</div>
    </div>
    <nav class="footer-nav">
      <a style="left:260px">Home</a>
      <a style="left:322px">About</a>
      <a style="left:386px">How It Works</a>
      <a style="left:497px">Product</a>
      <a style="left:575px">Resources</a>
      <a style="left:670px">Gallery</a>
      <a style="left:742px">Contact Us</a>
    </nav>
    <div class="social footer-social">
      <span class="dot-icon"></span>
      <span class="dot-icon"></span>
      <svg class="mail-icon" viewBox="0 0 16 11"><rect x="0.5" y="0.5" width="15" height="10" fill="none" stroke="#fff"/><path d="M0.5 0.5 L8 6.5 L15.5 0.5" fill="none" stroke="#fff"/></svg>
    </div>
  </footer>
</body>
</html>
```